Limbcraft Arbor Crew Bill Board Design

We are a high class full service tree company who specializes in artistic thinning and shaping of trees in Arizona. We want to re brand our company to catch our audiences attention and hook them into calling our company on the spot. We’ve been in business for 30 years and have never truly branded our company. We want our shirts trucks and billboards to match as well as our mailing advertisement so our clientele can recognize us immediately. We are starting with our billboard first and will be following with truck and shirt designs next. Attached is a example of what we are looking for and what we’ve had designed so far. This just isn’t good enough and needs revamped if at all posssible.
- Stencil

```html
<!DOCTYPE html>
<html lang="en">
<head>
<meta charset="UTF-8">
<title>Limbcraft Arbor Crew Billboard</title>
<link rel="stylesheet" href="https://fonts.googleapis.com/css2?family=Gochi+Hand&family=Raleway:ital,wght@0,300;1,300&family=Montserrat:wght@600&display=swap">
<style>
  :root {
    --backdrop: #2a3a66;
    --forest: #12904a;
    --forest-deep: #0c5a34;
    --meadow-light: #7fbf3a;
    --meadow-mid: #4d8f27;
    --meadow-dark: #1f4d14;
    --mist: #9fc29a;
    --paper: #f1f2f3;
    --ink-light: #ffffff;
  }
  html, body {
    margin: 0;
    width: 1200px;
    height: 900px;
    overflow: hidden;
    background: var(--backdrop);
  }
  .billboard {
    position: absolute;
    left: 50px;
    top: 181px;
    width: 1100px;
    height: 537px;
    display: block;
  }
  .headline-script {
    font-family: "Gochi Hand", cursive;
    fill: var(--ink-light);
  }
  .headline-light {
    font-family: "Raleway", sans-serif;
    font-weight: 300;
    fill: var(--ink-light);
  }
  .headline-light .place {
    font-style: italic;
  }
  .phone-number {
    font-family: "Montserrat", sans-serif;
    font-weight: 600;
    fill: var(--ink-light);
    letter-spacing: 1px;
  }
</style>
</head>
<body>
<svg class="billboard" viewBox="0 0 1100 537" xmlns="http://www.w3.org/2000/svg">
  <defs>
    <linearGradient id="meadowGradient" x1="0" y1="0" x2="0" y2="1">
      <stop offset="0" stop-color="var(--meadow-dark)"/>
      <stop offset="0.38" stop-color="var(--mist)"/>
      <stop offset="0.5" stop-color="var(--meadow-light)"/>
      <stop offset="1" stop-color="var(--meadow-dark)"/>
    </linearGradient>
    <linearGradient id="forestGradient" x1="0" y1="0" x2="0.6" y2="1">
      <stop offset="0" stop-color="var(--forest)"/>
      <stop offset="1" stop-color="var(--forest-deep)"/>
    </linearGradient>
    <clipPath id="boardClip"><rect width="1100" height="537"/></clipPath>
  </defs>

  <g clip-path="url(#boardClip)">
    <g class="meadow-photo" role="img" aria-label="Photo of a sunlit green meadow beneath the spreading branches of a large tree">
      <rect width="1100" height="537" fill="url(#meadowGradient)"/>
    </g>

    <g class="acacia-photo" role="img" aria-label="Green-toned photo of a shaped acacia tree standing alone on open grassland">
      <path d="M0 0 H640 A300 300 0 0 1 375 556 A300 300 0 0 1 0 290 Z" fill="url(#forestGradient)"/>
      <circle cx="375" cy="256" r="300" fill="url(#forestGradient)"/>
    </g>

    <path class="brush-ring" d="M95 420 A340 340 0 1 0 640 -60"
          fill="none" stroke="var(--paper)" stroke-width="78" stroke-linecap="round"/>

    <text class="headline-script" x="124" y="128" font-size="96">Artistic</text>
    <text class="headline-light" x="414" y="126" font-size="56">thinning</text>
    <text class="headline-light" x="182" y="196" font-size="52">and shaping of</text>
    <text class="headline-script" x="149" y="277" font-size="96">tees</text>
    <text class="headline-light" x="337" y="275" font-size="52">in <tspan class="place">Arizona</tspan></text>

    <g class="phone-icon" transform="translate(845 397)" fill="none" stroke="var(--ink-light)">
      <circle r="25" stroke-width="4"/>
      <path d="M-11 -13 C-15 -5 -10 8 2 14 L8 10 L3 3 L-1 5 C-5 2 -7 -3 -6 -6 L-2 -8 L-5 -15 Z"
            fill="var(--ink-light)" stroke="none"/>
      <path d="M2 -10 A9 9 0 0 1 10 -2" stroke-width="2.5"/>
      <path d="M3 -16 A15 15 0 0 1 16 -3" stroke-width="2.5"/>
    </g>

    <text class="phone-number" x="848" y="473" font-size="44" text-anchor="middle">602-555-0148</text>
  </g>
</svg>
</body>
</html>
```